2021 Halberd Ensemble Summer Music Institute & Festival

we need a brochure for the Summer music school and series of concerts. We want it to be modern, and informative. Please look at our web page:
http://academy.halberdensemble.org/halberd-summer-music-institute/

Target Market(s)

middle-class families with school and college children

Requirements
Must have
• text from the web page:
Also
http://halberdensemble.org/category/2021-halberd-summer-music-festival/
(this will be updated soon, but the events have to be listed in the brochure
Please use graphics from the pages and the attached files.

```html
<!DOCTYPE html>
<html lang="en">
<head>
<meta charset="utf-8">
<title>Halberd Ensemble Summer Music Institute &amp; Festival</title>
<link href="https://fonts.googleapis.com/css2?family=Montserrat:wght@500;700;800&family=Open+Sans:wght@400;600&display=swap" rel="stylesheet">
<style>
  :root {
    --ink: #1f1f1f;
    --body: #3a3a3a;
    --muted: #8a8a8a;
    --paper: #ffffff;
    --photo-dark: #2c3526;
    --photo-mid: #56624a;
    --photo-light: #b7a98a;
  }
  * { margin: 0; padding: 0; box-sizing: border-box; }
  html, body { width: 849px; height: 1200px; overflow: hidden; background: var(--paper); }
  .page {
    position: relative; width: 849px; height: 1200px;
    font-family: "Open Sans", Arial, sans-serif; color: var(--body);
    font-size: 12.5px; line-height: 21px;
  }
  .concert-photo {
    position: absolute; left: 68px; top: 14px; width: 376px; height: 612px;
    background: linear-gradient(160deg, var(--photo-light) 0%, var(--photo-mid) 38%, var(--photo-dark) 100%);
  }
  .details {
    position: absolute; left: 462px; top: 96px; width: 356px; text-align: justify;
  }
  .details p { margin-bottom: 21px; }
  .label {
    font-family: "Montserrat", Arial, sans-serif; font-weight: 800;
    color: var(--ink); letter-spacing: 0.3px;
  }
  .info-box {
    position: absolute; left: 113px; top: 686px; width: 736px; height: 232px;
    border-top: 3px solid var(--ink); border-left: 3px solid var(--ink);
    padding: 20px 30px 0 34px;
  }
  .info-box h2 {
    font-family: "Montserrat", Arial, sans-serif; font-weight: 800;
    font-size: 15px; color: var(--ink); letter-spacing: 0.4px; margin-bottom: 14px;
  }
  .info-box ul { list-style: none; }
  .info-box li { position: relative; padding-left: 12px; line-height: 21px; }
  .info-box li::before { content: "•"; position: absolute; left: 0; }
  .brand {
    position: absolute; left: 80px; top: 1140px; display: flex; align-items: center; gap: 8px;
    font-family: "Montserrat", Arial, sans-serif; font-weight: 700; font-size: 11px; color: var(--muted);
    letter-spacing: 0.5px;
  }
  .brand-dot { width: 12px; height: 12px; border-radius: 50%; background: var(--muted); }
  .contact {
    position: absolute; top: 1096px; display: flex; gap: 6px;
    font-family: "Montserrat", Arial, sans-serif; font-weight: 500; font-size: 7.5px; line-height: 11px;
    color: var(--ink); text-transform: uppercase; letter-spacing: 0.3px; white-space: nowrap;
  }
  .contact svg { flex: none; margin-top: 1px; }
  .contact-address { left: 372px; }
  .contact-phone { left: 536px; }
  .contact-email { right: 30px; }
</style>
</head>
<body>
<div class="page">
  <div class="concert-photo" role="img" aria-label="Photo of musicians performing an outdoor evening concert under trees"></div>

  <section class="details">
    <p><span class="label">INSTRUMENTS</span>: Strings: violin, viola, cello, double bass, piano</p>
    <p><span class="label">VENUE</span>: The Festival performances take place at St. Aldric Chapel in Farmington, Elmhurst Meeting House of Hartford, and the Corrigan Museum of Art in Hartford.</p>
    <p><span class="label">THE PROGRAM</span> is open to students and adults of all ages who demonstrate a good command of their instrument and are able to perform in a variety of chamber music and advanced orchestral settings.</p>
    <p>In order to be considered for solo performance opportunities, a student must come with a prepared repertoire including classical or romantic sonata, bravura piece, or concerto movement prepared prior to the start of the Institute. Piano accompaniment will be provided.</p>
  </section>

  <section class="info-box">
    <h2>IMPORTANT INFO</h2>
    <ul>
      <li>Arrival time between 9:30 to 10 am (earlier drop off may be arranged as needed)</li>
      <li>Pick up time 2 pm.</li>
      <li>Parents are required to provide transportation to camp and performance venues.</li>
      <li>Please bring your own masks and hand sanitizer as needed.</li>
      <li>We will provide additional sanitizer as needed.</li>
      <li>Classes will be limited to a maximum of 10 students.</li>
      <li>Please bring lunch and a snack.</li>
      <li>Students must have black folders labeled with their names, a notebook, staff paper, and a pencil on the first day of camp.</li>
      <li>Please bring a music stand.</li>
    </ul>
  </section>

  <div class="brand"><span class="brand-dot"></span>HALBERD ACADEMY</div>

  <div class="contact contact-address">
    <svg width="8" height="10" viewBox="0 0 8 10"><path d="M4 0a4 4 0 0 0-4 4c0 3 4 6 4 6s4-3 4-6a4 4 0 0 0-4-4z" fill="#1f1f1f"/><circle cx="4" cy="4" r="1.4" fill="#fff"/></svg>
    <span>St. Aldric Chapel<br>14 Larkspur Rd, Farmington<br>CT 06032, USA</span>
  </div>
  <div class="contact contact-phone">
    <svg width="9" height="9" viewBox="0 0 10 10"><path d="M2 0l2 2.5-1 1.2c.6 1.3 1.8 2.5 3.2 3.2l1.2-1L10 8l-1.5 2C4 9.7.3 6 0 1.5z" fill="#1f1f1f"/></svg>
    <span>(555) 014-2287 (cell)</span>
  </div>
  <div class="contact contact-email">
    <svg width="10" height="8" viewBox="0 0 10 8"><rect x="0.5" y="0.5" width="9" height="7" fill="none" stroke="#1f1f1f"/><path d="M0.5 0.8L5 4.5 9.5 0.8" fill="none" stroke="#1f1f1f"/></svg>
    <span>info@halberdensemble.org</span>
  </div>
</div>
</body>
</html>
```